Redesign of page from emergency manual

Please redesign this PDF to look better. Please don't include any stock photos. It must be legible. Making some words bold is probably a good idea.

Here are some things I like :

https://tarrowbooks.com.au/collections/frontpage/products/the-plk-v2-ebook

https://img-cd.vostramediafiles.com/qa-ejkwPLOTYY_SuCKbZNu411Qwgjv8YssPxEdzXN93hDkSRjLXK8WmfgbmrJW4ZZ3yUPK=w1052-h592-rw

```html
<!DOCTYPE html>
<html lang="en">
<head>
<meta charset="utf-8">
<title>Hypertension, Acute</title>
<link rel="stylesheet" href="https://fonts.googleapis.com/css2?family=Bebas+Neue&family=Oswald:wght@300;400&family=Arimo:wght@400;700&family=Open+Sans:wght@400&display=swap">
<style>
  :root {
    --cyan: #66e9fb;
    --cyan-light: #a0f3fd;
    --teal: #4bb3c4;
    --ink: #111111;
    --grey-band: #cccccc;
    --paper: #ffffff;
    --backdrop: #b3b3b3;
  }
  html, body { margin: 0; padding: 0; }
  body {
    width: 1200px; height: 1200px; overflow: hidden;
    background: var(--backdrop); position: relative;
  }
  .page {
    position: absolute; left: 0; top: 137px;
    width: 1528px; height: 1180px;
    background: var(--paper);
    transform: scale(0.78534); transform-origin: 0 0;
    color: var(--ink);
    font-family: "Arimo", Arial, sans-serif;
  }
  .page > * { position: absolute; }
  .bebas { font-family: "Bebas Neue", "Oswald", sans-serif; }

  .corner-tab { left: 0; top: 8px; width: 207px; height: 83px; background: var(--cyan); border-radius: 0 10px 10px 0; }
  .page-title { left: 229px; top: 14px; margin: 0; font-family: "Bebas Neue", sans-serif; font-weight: 400; font-size: 84px; line-height: 1; color: var(--teal); }
  .page-subtitle { left: 229px; top: 97px; width: 1210px; margin: 0; font-size: 29px; line-height: 1.12; }

  .side-band { left: 1456px; top: 0; width: 72px; height: 1180px; }
  .side-band svg { position: absolute; left: 0; top: 0; }
  .page-number { position: absolute; left: 0; width: 72px; top: 30px; text-align: center; font-family: "Bebas Neue", sans-serif; font-size: 52px; }
  .side-label { position: absolute; writing-mode: vertical-rl; font-family: "Bebas Neue", sans-serif; left: 0; width: 72px; display: flex; align-items: center; }
  .side-label.topic { top: 175px; font-size: 50px; line-height: 72px; }
  .side-label.revision { top: 945px; font-size: 34px; line-height: 72px; }

  .bp-table { left: 64px; top: 174px; width: 747px; height: 306px; box-sizing: border-box; border: 4px solid var(--cyan); border-radius: 18px; overflow: hidden; }
  .bp-table h2 { margin: 0; height: 66px; background: var(--cyan-light); font-family: "Bebas Neue", sans-serif; font-weight: 400; font-size: 54px; line-height: 72px; padding-left: 20px; border-radius: 0 0 14px 14px; }
  .bp-row { position: absolute; left: 0; right: 0; font-family: "Bebas Neue", sans-serif; font-size: 44px; line-height: 1; }
  .bp-row.head { top: 82px; }
  .bp-row span { position: absolute; }
  .bp-divider { position: absolute; left: 0; right: 0; height: 4px; background: var(--cyan); }

  .tips { left: 862px; top: 173px; width: 564px; height: 318px; background: var(--cyan); border-radius: 10px; }
  .tips-lead { position: absolute; left: 52px; top: 14px; width: 470px; margin: 0; font-weight: 700; font-size: 17.5px; line-height: 1.32; }
  .tips ul { position: absolute; left: 52px; top: 130px; width: 490px; margin: 0; padding: 0; list-style: none; font-size: 24px; line-height: 1.2; }
  .tips li { position: relative; margin-bottom: 26px; }
  .tips li::before { content: ""; position: absolute; left: -34px; top: 8px; width: 22px; height: 22px; border-radius: 50%; background: var(--paper); }

  .caution-label { left: 63px; top: 526px; width: 194px; height: 100px; background: var(--cyan); border-radius: 8px; font-family: "Bebas Neue", sans-serif; font-size: 48px; line-height: 100px; text-align: center; }
  .caution-text { left: 279px; top: 522px; width: 1146px; height: 106px; box-sizing: border-box; border: 3px solid var(--cyan); border-radius: 14px; padding: 6px 40px 0 16px; margin: 0; font-family: "Open Sans", Verdana, sans-serif; font-size: 20.5px; line-height: 1.33; letter-spacing: 0.2px; }

  .drug-card { top: 663px; height: 300px; box-sizing: border-box; border: 3px solid var(--cyan); border-radius: 12px; overflow: hidden; }
  .drug-card h3 { margin: 0; height: 76px; background: var(--teal); color: var(--paper); font-family: "Bebas Neue", sans-serif; font-weight: 400; font-size: 29px; line-height: 1.1; text-align: center; display: flex; align-items: center; justify-content: center; border-radius: 0 0 8px 8px; }
  .drug-card ul { margin: 0; padding: 10px 8px 0 24px; list-style: none; font-family: "Oswald", sans-serif; font-weight: 300; font-size: 20.5px; line-height: 1.48; }
  .drug-card li { position: relative; }
  .drug-card li::before { content: ""; position: absolute; left: -18px; top: 10px; width: 13px; height: 13px; border-radius: 50%; background: var(--cyan); }
  .drug-card .row-label { text-align: center; font-family: "Bebas Neue", sans-serif; font-size: 36px; margin-top: 63px; }

  .differential-band { left: 50px; top: 986px; width: 1376px; height: 50px; background: var(--grey-band); border-radius: 10px; font-family: "Bebas Neue", sans-serif; font-size: 31px; line-height: 54px; padding-left: 33px; box-sizing: border-box; }
  .differential { top: 1045px; margin: 0; padding: 0 0 0 24px; list-style: none; font-family: "Oswald", sans-serif; font-weight: 300; font-size: 21px; line-height: 28px; text-transform: uppercase; }
  .differential li { position: relative; }
  .differential li::before { content: ""; position: absolute; left: -24px; top: 8px; width: 13px; height: 13px; border-radius: 50%; background: var(--cyan); }
</style>
</head>
<body>
<main class="page">
  <div class="corner-tab"></div>
  <h1 class="page-title">Hypertension, Acute</h1>
  <p class="page-subtitle">SUSTAINED HIGH BLOOD PRESSURE REFRACTORY TO TREATING REVERSIBLE CAUSES</p>

  <aside class="side-band">
    <svg width="72" height="1180" viewBox="0 0 72 1180" aria-hidden="true">
      <polygon points="0,0 72,0 72,93 0,133" fill="#66e9fb"/>
      <polygon points="0,170 72,128 72,846 0,886" fill="#66e9fb"/>
      <polygon points="0,925 72,882 72,1180 0,1180" fill="#66e9fb"/>
    </svg>
    <div class="page-number">12</div>
    <div class="side-label topic">HYPERTENSION, ACUTE</div>
    <div class="side-label revision">REVISION 10. 2023</div>
  </aside>

  <section class="bp-table">
    <h2>Hypertensive Blood Pressure Range*</h2>
    <div class="bp-row head"><span style="left:24px">AGE (YR)</span><span style="left:275px">SYSTOLIC</span><span style="left:550px">DIASTOLIC</span></div>
    <div class="bp-divider" style="top:132px"></div>
    <div class="bp-row" style="top:142px"><span style="left:29px">NEWBORN</span><span style="left:352px">&gt;97</span><span style="right:16px">&gt;70</span></div>
    <div class="bp-divider" style="top:187px"></div>
    <div class="bp-row" style="top:199px"><span style="left:69px">1-3</span><span style="left:350px">&gt;105</span><span style="right:16px">&gt;61</span></div>
    <div class="bp-divider" style="top:243px"></div>
    <div class="bp-row" style="top:256px"><span style="left:63px">4-12</span><span style="left:350px">&gt;113</span><span style="right:16px">&gt;86</span></div>
  </section>

  <section class="tips">
    <p class="tips-lead">IN PEDIATRICS, HYPERTENSION IS ALMOST ALWAYS TREATED BY ADDRESSING LIKELY CAUSES SUCH AS LIGHT ANESTHESIA OR MEASUREMENT ERROR:</p>
    <ul>
      <li>Ensure correct BP cuff size: cuff bladder width ~ 40% of limb circumference</li>
      <li>Ensure arterial line transducer is at level of heart. Consider placing arterial line if not already present</li>
    </ul>
  </section>

  <div class="caution-label">* Caution:</div>
  <p class="caution-text">Anti-hypertensive drugs are almost never needed for routine pediatric cases. These medications are used almost exclusively for specialized cardiac, neurosurgical, or endocrine (pheochromocytoma) cases. Consult an expert before use. Rule-out increased ICP.</p>

  <section class="drug-card" style="left:54px;width:216px">
    <h3>Action</h3>
    <div class="row-label">Drug (IV Dosing)</div>
  </section>
  <section class="drug-card" style="left:283px;width:258px">
    <h3>Direct Smooth<br>Muscle Relaxation</h3>
    <ul>
      <li>Sodium nitroprusside 0.5-10 MICROgrams/kg/min</li>
      <li>HydrALAZINE 0.1-0.2 mg/kg (adult dose 5-10 mg)</li>
    </ul>
  </section>
  <section class="drug-card" style="left:571px;width:258px">
    <h3>β-Adrenergic<br>Blockade</h3>
    <ul style="line-height:1.28">
      <li>Esmolol 100-500 MICROgrams/kg over 5 min, then 25-300 MICROgrams/kg/min</li>
      <li>Labetalol (also α effect) 0.2-1 mg/kg q 10 min; 0.4-3 mg/kg/hour (infusion)</li>
    </ul>
  </section>
  <section class="drug-card" style="left:863px;width:258px">
    <h3>Calcium Channel<br>Blockade</h3>
    <ul>
      <li>niCARdipine<br>0.5-5 MICROgrams/kg/min</li>
      <li>Clevidipine<br>0.5-3.5 MICROgrams/kg/min</li>
    </ul>
  </section>
  <section class="drug-card" style="left:1161px;width:258px">
    <h3>D1-Dopamine<br>Agonist</h3>
    <ul>
      <li>Fenoldopam 0.2-0.8 MICROgrams/kg/min</li>
    </ul>
  </section>

  <div class="differential-band">Consider Differential (Partial):</div>
  <ul class="differential" style="left:63px;width:360px">
    <li>Light anesthesia (consider vaporizer or infusion pump empty or malfunctioning)</li>
    <li>Hypercarbia</li>
  </ul>
  <ul class="differential" style="left:493px;width:300px">
    <li>Hypoxemia</li>
    <li>Arterial line transducer too low or BP cuff too small</li>
    <li>Withdrawal (EtOH or opioid)</li>
  </ul>
  <ul class="differential" style="left:897px;width:300px;line-height:26px">
    <li>Thyroid storm</li>
    <li>Pheochromocytoma</li>
    <li>Drug error</li>
  </ul>
</main>
</body>
</html>
```